Building company buisness cards

We are looking for a sharp modern new look for our business cards.
We are a New Zealand based company that specialises in house and land packages.
We have attached a photo of the current logo and would like to see if it can be improved somehow if needed.
We are open to any colours but we have chosen green at this stage.
Feel free to change the font and make the logo smarter looking.
Play with the colours and see what looks best.

We want a card that looks so good know one will want to throw it away!

Target Market(s)

Home buyers

Industry/Entity Type

Building

Contact Information for Business Card

Garth Ellery
0219364028
gellery@tidewaterhomecraft.co.nz
tidewaterhomecraft.co.nz

Font styles to use
Serif
Sans Serif

Colors

Designer to choose colors to be used in the design.

Requirements
Must have
• Logo and company name on one side, details on the other side
Nice to have
• Color codes for the original green are HEX #4a8028, RGB(74,128,40), CMYK(42,0,69,50)
• Round corners, Raised and/or spot UV

```html
<!DOCTYPE html>
<html lang="en">
<head>
<meta charset="utf-8">
<title>Tidewater Homecraft – Business Cards</title>
<link href="https://fonts.googleapis.com/css2?family=Montserrat:wght@600;700&family=Roboto+Condensed:wght@400&display=swap" rel="stylesheet">
<style>
  :root {
    --brand-green: #4a8028;
    --brand-green-deep: #3a6a22;
    --card-white: #ffffff;
    --card-white-shade: #e9e9e9;
    --ink-grey: #555555;
    --backdrop: #3b3b3b;
    --on-green: #e6ece2;
  }
  * { margin: 0; padding: 0; box-sizing: border-box; }
  html, body {
    width: 1200px; height: 900px; overflow: hidden;
    background: var(--backdrop);
  }
  .sheet {
    position: relative; width: 1200px; height: 900px;
    display: flex; flex-direction: column; align-items: center; justify-content: center;
    gap: 52px;
  }
  .card {
    position: relative; width: 640px; height: 366px;
    border-radius: 22px; overflow: hidden;
    box-shadow: 0 10px 24px rgba(0,0,0,0.35);
  }

  /* Details side */
  .card--details {
    background: radial-gradient(ellipse at 40% 35%, var(--card-white) 40%, var(--card-white-shade) 100%);
  }
  .holder {
    position: absolute; right: 330px; top: 138px; text-align: right;
  }
  .holder__name {
    font-family: "Montserrat", sans-serif; font-weight: 700;
    font-size: 30px; color: var(--brand-green); letter-spacing: -0.3px; line-height: 1.1;
  }
  .holder__role {
    font-family: "Roboto Condensed", sans-serif; font-size: 15px;
    color: var(--ink-grey); margin-top: 2px;
  }
  .divider {
    position: absolute; left: 326px; top: 158px; width: 2px; height: 86px;
    background: var(--brand-green);
  }
  .contacts {
    position: absolute; left: 346px; top: 160px; list-style: none;
    font-family: "Roboto Condensed", sans-serif; font-size: 17px; color: var(--ink-grey);
  }
  .contacts li { display: flex; align-items: center; gap: 9px; height: 27px; }
  .contacts svg { width: 13px; height: 13px; flex: none; }

  /* Brand side */
  .card--brand {
    background: linear-gradient(135deg, var(--brand-green) 0%, var(--brand-green-deep) 100%);
  }
  .brand {
    position: absolute; left: 0; right: 0; top: 120px; text-align: center;
    display: flex; align-items: center; justify-content: center; gap: 16px;
  }
  .brand__mark {
    width: 30px; height: 30px; background: var(--on-green);
  }
  .brand__name {
    font-family: "Montserrat", sans-serif; font-weight: 700;
    font-size: 44px; color: var(--on-green); letter-spacing: 0.5px;
  }
  .brand__web {
    position: absolute; left: 0; right: 0; top: 210px; text-align: center;
    font-family: "Roboto Condensed", sans-serif; font-size: 20px; color: var(--on-green);
  }
</style>
</head>
<body>
<main class="sheet">
  <section class="card card--details">
    <div class="holder">
      <p class="holder__name">Garth Ellery</p>
      <p class="holder__role">Founder</p>
    </div>
    <div class="divider"></div>
    <ul class="contacts">
      <li>
        <svg viewBox="0 0 24 24" fill="var(--brand-green)"><path d="M6.6 10.8a15.1 15.1 0 0 0 6.6 6.6l2.2-2.2a1 1 0 0 1 1-.25 11.4 11.4 0 0 0 3.6.6 1 1 0 0 1 1 1V20a1 1 0 0 1-1 1A17 17 0 0 1 3 4a1 1 0 0 1 1-1h3.5a1 1 0 0 1 1 1 11.4 11.4 0 0 0 .6 3.6 1 1 0 0 1-.25 1z"/></svg>
        <span>0219364028</span>
      </li>
      <li>
        <svg viewBox="0 0 24 24" fill="none" stroke="var(--brand-green)" stroke-width="2.4"><rect x="2" y="5" width="20" height="14" rx="1"/><path d="M2 6l10 7 10-7"/></svg>
        <span>gellery@tidewaterhomecraft.co.nz</span>
      </li>
      <li>
        <svg viewBox="0 0 24 24" fill="none" stroke="var(--brand-green)" stroke-width="2.2"><circle cx="12" cy="12" r="10"/><path d="M2 12h20M12 2c3 3 3 17 0 20M12 2c-3 3-3 17 0 20"/></svg>
        <span>www.tidewaterhomecraft.co.nz</span>
      </li>
    </ul>
  </section>

  <section class="card card--brand">
    <div class="brand">
      <span class="brand__mark"></span>
      <span class="brand__name">Tidewater Homecraft</span>
    </div>
    <p class="brand__web">www.tidewaterhomecraft.co.nz</p>
  </section>
</main>
</body>
</html>
```